Copper Lantern LLC Business Card

We need a business card design for a newco in Texas. We are a team of professionals who join start ups as founders and help launch their businesses, which are primarily related to food and beverage and the service side of the industry. We love local and craft and are partners in businesses in the local meat, BBQ and Burger, fine dining, and beverage alcohol businesses. Our specialty is finance and the business side of start ups, including assisting with capital raises as principals, not brokers. We do not currently have any logos or graphics for this entity. Our values include helping people succeed, rooting for the underdog, healthy food, the environment and being good citizens.

Target Market(s)

Everybody but also Angel Investors, CPAs, Bankers, Entrepreneurs

Industry/Entity Type

Business

Contact Information for Business Card

Fields for Business Name, Title, Email Address, Phone Number. Place to add mailing address and web domain later.

Font styles to use
Sans Serif

Colors

Designer to choose colors to be used in the design.

Requirements
Should not have
• Pictures of booze bottles or drinks thought there could be a social scene that does not strictly focus on those. No cows, cowboy hats or ranches. We are not a Wall Street type entity so no huge office buildings or skylines.

```html
<!DOCTYPE html>
<html lang="en">
<head>
<meta charset="utf-8">
<title>Copper Lantern LLC – Business Card</title>
<link rel="stylesheet" href="https://fonts.googleapis.com/css2?family=Michroma&family=Mulish:ital,wght@0,300;0,400;1,300&display=swap">
<style>
  :root {
    --page: #ffffff;
    --card: #1b1b1b;
    --card-glow: #3a3a3a;
    --ink: #e2e2e2;
    --ink-soft: #c9c9c9;
    --gold: #e0a52a;
    --shadow: rgba(0, 0, 0, 0.45);
  }
  * { box-sizing: border-box; margin: 0; padding: 0; }
  html, body {
    width: 1200px;
    height: 984px;
    overflow: hidden;
    background: var(--page);
  }
  .canvas {
    position: relative;
    width: 1200px;
    height: 984px;
  }
  .card {
    position: absolute;
    width: 483px;
    height: 825px;
    background: var(--card);
    box-shadow: 14px 22px 30px var(--shadow);
    color: var(--ink);
    text-align: center;
  }
  .card--front {
    left: 49px;
    top: 49px;
    background:
      radial-gradient(circle at 50% 36%, var(--card-glow) 0, rgba(27,27,27,0) 190px),
      var(--card);
  }
  .card--back {
    left: 624px;
    top: 64px;
  }
  .brand-mark {
    position: absolute;
    left: 50%;
    border-radius: 50%;
    background: var(--gold);
    transform: translateX(-50%);
  }
  .card--front .brand-mark { top: 205px; width: 96px; height: 96px; }
  .card--back .brand-mark { top: 60px; width: 44px; height: 44px; }
  .brand-name {
    position: absolute;
    left: 0;
    right: 0;
    font-family: "Michroma", sans-serif;
    font-variant: small-caps;
    color: var(--ink-soft);
    line-height: 1;
    white-space: nowrap;
  }
  .card--front .brand-name { top: 388px; font-size: 27px; }
  .card--back .brand-name { top: 164px; font-size: 19px; }
  .person-name {
    position: absolute;
    left: 0;
    right: 0;
    top: 290px;
    font-family: "Michroma", sans-serif;
    font-variant: small-caps;
    font-size: 34px;
    line-height: 60px;
    color: var(--ink);
  }
  .person-title {
    position: absolute;
    left: 0; right: 0;
    top: 408px;
    font-family: "Mulish", sans-serif;
    font-style: italic;
    font-weight: 300;
    font-size: 27px;
    color: var(--ink-soft);
  }
  .contact-phone {
    position: absolute;
    left: 0; right: 0;
    top: 494px;
    font-family: "Mulish", sans-serif;
    font-weight: 300;
    font-size: 33px;
    color: var(--ink);
  }
  .contact-email {
    position: absolute;
    left: 0; right: 0;
    top: 546px;
    font-family: "Mulish", sans-serif;
    font-weight: 300;
    font-size: 25px;
    color: var(--ink-soft);
  }
  .contact-address {
    position: absolute;
    left: 0; right: 0;
    top: 700px;
    font-family: "Mulish", sans-serif;
    font-style: italic;
    font-weight: 300;
    font-size: 21px;
    line-height: 29px;
    color: var(--ink-soft);
  }
</style>
</head>
<body>
<main class="canvas">
  <section class="card card--front" aria-label="Card front">
    <span class="brand-mark" aria-hidden="true"></span>
    <h1 class="brand-name">Copper Lantern LLC</h1>
  </section>

  <section class="card card--back" aria-label="Card back">
    <span class="brand-mark" aria-hidden="true"></span>
    <p class="brand-name">Copper Lantern LLC</p>
    <h2 class="person-name">Firstname<br>Lastname</h2>
    <p class="person-title">Fancy Title</p>
    <p class="contact-phone">789.456.3210</p>
    <p class="contact-email">email@website.com</p>
    <p class="contact-address">123 Anywhere Street<br>City, State 99999</p>
  </section>
</main>
</body>
</html>
```